Lanternwick Home & Commercial Services, Inc.

I need a facebook design for our commercial repair/maintenance company based in Austin, TX. We offer many commercial services:plumbing, HVAC, Carpet/Air duct cleaning, Fire and water restoration, and general maintenance services
Our customer base includes commercial government organizations as NRDX and Camp Tolliver. We serve as the general contractor for these organizations and can handle any scope of work. ie flooring install, drywall, asbestos abatement, and mold removal.
We need a facebook design that communicates to our customer that we strive in customer satisfaction and pricing.
Updates
Logo uploaded. I will also upload photos for some job that have been completed.
I don't have images of our employees actively doing a job. I do have before and after picture that intend to post after fb cover is created.
I like the designs. I will sit with my husband tonight to brainstorm or select a design. Keep submitting, please.

```html
<!DOCTYPE html>
<html lang="en">
<head>
<meta charset="utf-8">
<title>Lanternwick Home &amp; Commercial Services – Cover</title>
<link href="https://fonts.googleapis.com/css2?family=Open+Sans:wght@400;600;700&display=swap" rel="stylesheet">
<style>
  :root {
    --page-bg: #eef0f3;
    --green-deep: #0f4d1c;
    --green-mid: #1f7a30;
    --green-light: #3aa04a;
    --gold: #c8b88a;
    --gold-text: #e3d6a8;
    --white: #ffffff;
    --ink: #1a1a1a;
    --frame: #b9bec7;
    --navy: #3b4a63;
    --slate: #6f7d8f;
    --steel: #a9b3bf;
    --chrome: #dfe5ec;
    --skin: #c89a7a;
    --amber: #e0b23a;
    --teal: #4d6e6a;
  }
  html, body {
    margin: 0;
    width: 1200px;
    height: 644px;
    overflow: hidden;
    background: var(--page-bg);
    font-family: "Open Sans", Arial, sans-serif;
  }
  .page { position: relative; width: 1200px; height: 644px; }
  .cover {
    position: absolute;
    left: 47px;
    top: 40px;
    width: 1105px;
    height: 410px;
    display: block;
  }
  .profile-card {
    position: absolute;
    left: 76px;
    top: 294px;
    width: 218px;
    height: 218px;
    background: var(--white);
    border: 1px solid var(--frame);
    box-sizing: border-box;
    padding: 8px;
  }
  .profile-card__inner {
    width: 100%;
    height: 100%;
    display: flex;
    flex-direction: column;
    align-items: center;
    justify-content: center;
    gap: 6px;
  }
  .brand-row { display: flex; align-items: center; gap: 6px; }
  .brand-mark { width: 14px; height: 14px; background: var(--green-deep); }
  .brand-name { font-weight: 700; font-size: 22px; color: var(--green-deep); letter-spacing: 0.5px; }
  .brand-tag { font-weight: 700; font-size: 9.5px; color: var(--green-deep); letter-spacing: 0.3px; }
  .page-name {
    position: absolute;
    left: 329px;
    top: 462px;
    margin: 0;
    font-weight: 700;
    font-size: 20px;
    color: var(--ink);
  }
</style>
</head>
<body>
<main class="page">
  <svg class="cover" viewBox="0 0 850 315" xmlns="http://www.w3.org/2000/svg">
    <defs>
      <linearGradient id="panelGreen" x1="0" y1="0" x2="1" y2="1">
        <stop offset="0" stop-color="#3aa04a"/>
        <stop offset="0.6" stop-color="#1f7a30"/>
        <stop offset="1" stop-color="#0f4d1c"/>
      </linearGradient>
      <linearGradient id="toneWorker" x1="0" y1="0" x2="0" y2="1">
        <stop offset="0" stop-color="#f2f2f2"/>
        <stop offset="0.45" stop-color="#c89a7a"/>
        <stop offset="1" stop-color="#3b4a63"/>
      </linearGradient>
      <linearGradient id="toneHardHat" x1="0" y1="0" x2="0" y2="1">
        <stop offset="0" stop-color="#e0b23a"/>
        <stop offset="0.45" stop-color="#c89a7a"/>
        <stop offset="1" stop-color="#4d6e6a"/>
      </linearGradient>
      <linearGradient id="toneWrench" x1="0" y1="0" x2="1" y2="1">
        <stop offset="0" stop-color="#3b4a63"/>
        <stop offset="0.5" stop-color="#b33a2e"/>
        <stop offset="1" stop-color="#2e3a4f"/>
      </linearGradient>
      <linearGradient id="toneSockets" x1="0" y1="0" x2="1" y2="1">
        <stop offset="0" stop-color="#2b2f36"/>
        <stop offset="0.5" stop-color="#a9b3bf"/>
        <stop offset="1" stop-color="#2b2f36"/>
      </linearGradient>
      <linearGradient id="toneChrome" x1="0" y1="0" x2="1" y2="1">
        <stop offset="0" stop-color="#ffffff"/>
        <stop offset="0.55" stop-color="#c5ced8"/>
        <stop offset="1" stop-color="#eef2f6"/>
      </linearGradient>
      <linearGradient id="toneSink" x1="0" y1="0" x2="0" y2="1">
        <stop offset="0" stop-color="#e6e9ee"/>
        <stop offset="0.6" stop-color="#9aa4b0"/>
        <stop offset="1" stop-color="#2f343b"/>
      </linearGradient>
      <linearGradient id="toneBath" x1="0" y1="0" x2="0" y2="1">
        <stop offset="0" stop-color="#f4f1ea"/>
        <stop offset="1" stop-color="#d9cdb8"/>
      </linearGradient>
    </defs>
    <rect width="850" height="315" fill="var(--white)"/>

    <g class="photo-grid">
      <rect x="0" y="0" width="103" height="91" fill="url(#toneWorker)" role="img" aria-label="Smiling technician in cap"/>
      <rect x="106" y="0" width="100" height="91" fill="url(#toneWrench)" role="img" aria-label="Worker holding a red pipe wrench"/>
      <rect x="210" y="0" width="100" height="91" fill="url(#toneHardHat)" role="img" aria-label="Smiling worker in hard hat"/>
      <rect x="0" y="95" width="103" height="101" fill="url(#toneSockets)" role="img" aria-label="Socket wrench set"/>
      <rect x="106" y="95" width="100" height="101" fill="url(#toneHardHat)" role="img" aria-label="Worker in hard hat giving thumbs up"/>
      <rect x="210" y="95" width="100" height="101" fill="url(#toneWorker)" role="img" aria-label="Technician with cordless drill"/>
      <rect x="0" y="200" width="103" height="100" fill="url(#toneChrome)" role="img" aria-label="Tools close-up"/>
      <rect x="106" y="200" width="100" height="100" fill="url(#toneSockets)" role="img" aria-label="Tool detail"/>
      <rect x="210" y="200" width="100" height="100" fill="url(#toneHardHat)" role="img" aria-label="Worker in hard hat and safety glasses"/>

      <rect x="314" y="0" width="127" height="35" fill="url(#toneSink)" role="img" aria-label="Wrench on pipe"/>
      <rect x="446" y="0" width="128" height="35" fill="url(#toneChrome)" role="img" aria-label="Chrome faucet"/>
      <rect x="580" y="0" width="130" height="35" fill="url(#toneChrome)" role="img" aria-label="Faucet detail"/>
      <rect x="314" y="42" width="127" height="126" fill="url(#toneChrome)" role="img" aria-label="Chrome shut-off valve"/>
      <rect x="446" y="42" width="128" height="126" fill="url(#toneWrench)" role="img" aria-label="Plumber holding a pipe wrench"/>
      <rect x="580" y="42" width="130" height="126" fill="url(#toneChrome)" role="img" aria-label="Chrome mixer tap"/>
      <rect x="314" y="174" width="127" height="126" fill="url(#toneSink)" role="img" aria-label="Plumber fixing sink drain pipes"/>
      <rect x="446" y="174" width="128" height="126" fill="url(#toneBath)" role="img" aria-label="White toilet in bathroom"/>
      <rect x="580" y="174" width="130" height="126" fill="url(#toneSink)" role="img" aria-label="Pipes under a sink"/>
    </g>

    <polygon class="thanks-panel" points="701,0 850,0 850,315 612,315" fill="url(#panelGreen)"/>
    <rect class="cover__band" x="0" y="305" width="850" height="10" fill="var(--green-deep)"/>

    <g class="thanks-panel__content" font-family="Open Sans, Arial, sans-serif">
      <g class="approval-icon">
        <rect x="723" y="104" width="56" height="56" rx="10" fill="var(--white)"/>
        <path d="M735 133 L747 145 L768 118" fill="none" stroke="var(--green-mid)" stroke-width="7" stroke-linecap="round" stroke-linejoin="round"/>
      </g>
      <text x="751" y="191" text-anchor="middle" fill="var(--white)" font-weight="600" font-size="17">Thank you</text>
      <text x="732" y="208" text-anchor="middle" fill="var(--white)" font-weight="600" font-size="13">for your</text>
      <rect x="763" y="197" width="30" height="14" rx="2" fill="var(--white)"/>
      <rect x="766" y="200" width="8" height="8" fill="var(--green-mid)"/>
      <text x="777" y="208" fill="var(--green-deep)" font-weight="700" font-size="7.5">Like</text>
      <rect x="625" y="247" width="225" height="2" fill="var(--gold)"/>
      <text x="742" y="273" text-anchor="middle" fill="var(--gold-text)" font-size="11.5" letter-spacing="0.3">www.lanternwickhcs.com</text>
      <text x="742" y="288" text-anchor="middle" fill="var(--gold-text)" font-size="11.5" letter-spacing="0.3">info@lanternwickhcs.com</text>
    </g>
  </svg>

  <div class="profile-card">
    <div class="profile-card__inner">
      <div class="brand-row">
        <span class="brand-mark"></span>
        <span class="brand-name">LANTERNWICK</span>
      </div>
      <span class="brand-tag">HOME &amp; COMMERCIAL SERVICES</span>
    </div>
  </div>

  <p class="page-name">www.lanternwickhcs.com</p>
</main>
</body>
</html>
```